Chinese Herbal and Roots Shop design

Hello Designers,

We are a herbal startup company which sells Chinese Herbal Products. we are looking for a responsive and unqiue Ecommerce web design.
Our business name is velorin and our area of business cut across the entire United States.

We don't have a logo at the moment and designers who come up with a great logo is more likely to be awarded winner of the consent.

The design needs to be completely custom design and we are not after just a template design. Please be creative and at the same time design have to be professionally looking and easy to navigate.
A theme which suits a herbal products are desired. We are open to different colors excpet RED and PINK.

NAVIGATION
Header -
Home, products, offers, Blog, cart, login/account

Footer -
Please refer to other Ecommerce websites

Page requires:
HOME PAGE
1. slider(Highlist products)
2. FEATURE PRODUCTS
3. Latest products
4. Most selling products
5. Deal of the day
6. Email capture (Newsletter/signup)
7. Social media links
8. Footer

PRODUCT PAGE
All the products will be present here with required details (price, short note and offers if any)

PRODUCT DETAILS PAGE
A well designed detailed page for a particular product covers the details of the price, increment, short description, purchase and other add to cart button. A section with similar products should be listed below aswell.

Industry/Entity Type

It Company

Coding

Coded - Design and coding required

```html
<!DOCTYPE html>
<html lang="en">
<head>
<meta charset="utf-8">
<title>Velorin — Herbal &amp; Roots Shop</title>
<link rel="stylesheet" href="https://fonts.googleapis.com/css2?family=Cinzel:wght@400;700&family=Lato:wght@400;700&display=swap">
<style>
:root{
  --page-bg:#eceeec;
  --brown:#7c5a1e;
  --brown-dark:#5a3a12;
  --heading-brown:#5b3b10;
  --leaf:#5aa51e;
  --leaf-deep:#2f6d14;
  --lime:#cbdc6c;
  --lime-btn:#d9ee3a;
  --ink:#222;
  --muted:#777;
  --white:#fff;
  --black-bar:#262626;
  --tag:#e6e08a;
}
*{box-sizing:border-box;margin:0;padding:0}
html,body{width:1200px;height:2699px;overflow:hidden}
body{position:relative;background:linear-gradient(90deg,#e6e8e6,#f3f4f3 50%,#e6e8e6);font-family:"Lato",Arial,sans-serif;color:var(--ink)}
.abs{position:absolute}

.greenery{position:absolute;border-radius:40% 40% 45% 45%;background:radial-gradient(ellipse at center,#4f9a2a 0%,#6cae3c 45%,rgba(120,180,80,.55) 70%,rgba(236,238,236,0) 100%)}

.brand{position:absolute;left:170px;top:38px;display:flex;align-items:center;gap:14px}
.brand-dot{width:30px;height:30px;border-radius:50%;background:var(--brown-dark)}
.brand-name{font-family:"Cinzel",serif;font-size:50px;font-weight:700;color:var(--brown-dark);line-height:1}

.main-nav{position:absolute;left:173px;top:148px;width:858px;height:32px;background:var(--brown);display:flex;align-items:center;padding:0 22px;font-size:12.5px;font-weight:700;color:var(--white)}
.main-nav a{color:var(--white);text-decoration:none}
.nav-links{display:flex;gap:12px;align-items:center}
.nav-links .sep{width:5px;height:5px;border-radius:50%;background:var(--white)}
.nav-user{margin-left:auto;display:flex;gap:40px;align-items:center;font-weight:400;font-size:12px}
.nav-user span{display:flex;align-items:center;gap:10px}

.hero{position:absolute;left:173px;top:180px;width:858px;height:373px;background:linear-gradient(90deg,#fff 0%,#f4f4f2 100%);box-shadow:0 2px 8px rgba(0,0,0,.15);overflow:hidden}
.hero-photo{position:absolute;left:300px;top:0;width:558px;height:373px;background:radial-gradient(circle at 60% 55%,#4b6a2a 0%,#7c8d52 25%,#c9c3b0 55%,#f1efea 80%)}
.hero-title{position:absolute;left:90px;top:78px;font-family:"Cinzel",serif;color:var(--brown-dark);text-align:right;line-height:1}
.hero-title .small{display:block;font-family:"Lato",sans-serif;font-size:28px;color:#3a2a10;margin-right:14px}
.hero-title .big{display:block;font-size:52px;letter-spacing:4px;margin-top:6px}
.hero-title .green{display:block;font-size:52px;letter-spacing:2px;color:var(--leaf);margin-top:2px}

.intro{position:absolute;left:290px;top:603px;width:650px;text-align:center;font-size:12.5px;line-height:21px;color:#333}
.intro-cta{position:absolute;left:432px;top:691px;width:345px;height:33px}
.intro-cta::before,.intro-cta::after{content:"";position:absolute;top:16px;width:70px;height:1px;background:#bbb}
.intro-cta::before{left:0}.intro-cta::after{right:0}
.btn-read{position:absolute;left:68px;top:0;width:208px;height:33px;border-radius:17px;background:var(--lime-btn);border:2px solid var(--leaf-deep);font-size:12.5px;color:#333;display:flex;align-items:center;justify-content:center}

.panel{position:absolute;left:173px;top:778px;width:858px;height:1470px;background:var(--white);box-shadow:0 0 10px rgba(0,0,0,.12)}
.section-title{position:absolute;left:21px;font-family:"Cinzel",serif;font-weight:700;font-size:21px;letter-spacing:1.5px;color:var(--heading-brown)}
.section-rule{position:absolute;left:21px;width:808px;height:2px;background:#eee}

.card{position:absolute;width:173px;height:288px;background:var(--brown)}
.card-tag{position:absolute;top:10px;width:100%;text-align:center;font-family:"Cinzel",serif;font-weight:700;font-size:17px;letter-spacing:1.5px;color:var(--tag)}
.card-photo{position:absolute;left:25px;top:50px;width:123px;height:126px}
.photo-jar{background:radial-gradient(circle at 50% 45%,#f3f3f3 0%,#c8c8c8 45%,#8c2222 46%,#6e1a1a 70%,#d8d8d8 72%)}
.photo-box{background:linear-gradient(160deg,#e6ece8,#6a9a8a 45%,#2d5a4e 60%,#dfe6e0)}
.photo-bottle{background:linear-gradient(180deg,#4a4a4a 0%,#eef3f3 15%,#5f8a3a 55%,#c8d8e0 90%)}
.photo-powder{background:linear-gradient(180deg,#f4f4f4 0%,#e8e8e8 40%,#2f7a3a 60%,#c9a25c 80%,#a57a3a 100%)}
.card-info{position:absolute;left:0;top:191px;width:100%;height:70px;background:var(--lime);text-align:center;padding-top:4px;font-size:15px;line-height:16px;color:#222}
.card-info .price{font-weight:700;font-size:16px;margin-bottom:2px}
.card-buy{position:absolute;left:0;top:261px;width:100%;height:27px;background:var(--black-bar);color:var(--white);font-family:"Cinzel",serif;font-weight:700;font-size:15px;display:flex;align-items:center;justify-content:center;letter-spacing:.5px}

.trust{position:absolute;left:65px;top:1265px;display:flex;align-items:center;gap:14px}
.trust-badge{width:54px;height:64px;background:#8a8a8a;border-radius:6px 6px 27px 27px}
.trust-text{font-size:17px;line-height:23px;color:#222}
.trust-text b{color:var(--leaf-deep);font-weight:700;display:block}
.follow{position:absolute;left:70px;top:1363px;font-family:"Cinzel",serif;font-size:13px;color:#222}
.social{position:absolute;left:68px;top:1393px;display:flex;gap:4px}
.social span{width:30px;height:30px;border-radius:50%;background:#6a4a1a;border:3px solid var(--leaf)}
.divider-v{position:absolute;left:367px;top:1247px;width:1px;height:117px;background:#ddd}

.newsletter-title{position:absolute;left:417px;top:1273px;width:440px;text-align:center;font-family:"Cinzel",serif;font-weight:700;font-size:18px;color:var(--heading-brown)}
.newsletter-title::before,.newsletter-title::after{content:"";position:absolute;top:11px;width:52px;height:1px;background:#ccc}
.newsletter-title::before{left:90px}.newsletter-title::after{right:90px}
.newsletter-text{position:absolute;left:417px;top:1316px;width:440px;text-align:center;font-size:15px;line-height:22px;color:#888}
.newsletter-text b{color:#555}
.newsletter-form{position:absolute;left:417px;top:1382px;width:369px;height:36px;border-radius:18px;background:#ddd;border:1px solid #ccc}
.newsletter-form .field{position:absolute;left:16px;top:9px;font-size:14px;color:#fff}
.newsletter-form .ok{position:absolute;right:0;top:0;width:56px;height:34px;border-radius:17px;background:#f4f4f4;border:1px solid #ccc;font-size:14px;font-weight:700;color:#666;display:flex;align-items:center;justify-content:center}

.deal{position:absolute;left:173px;top:2245px;width:858px;height:212px;background:radial-gradient(ellipse at 30% 40%,#9bd06a 0%,#5da033 40%,#2d6a1a 100%);overflow:hidden}
.deal-photo{position:absolute;right:0;top:0;width:250px;height:212px;background:linear-gradient(90deg,rgba(255,255,255,0) 0%,rgba(245,240,235,.75) 45%,#e8e2dc 70%,#2a2a2a 100%)}
.deal-text{position:absolute;left:40px;top:34px;font-family:"Cinzel",serif;font-weight:700;color:var(--white);line-height:1}
.deal-text .h1{font-size:28px;letter-spacing:1px}
.deal-text .h2{font-size:21px;margin-top:10px;line-height:25px;color:#f1f1e0}
.deal-text .h3{font-size:28px;margin-top:13px}
.deal-buy{position:absolute;left:329px;top:138px;width:132px;height:31px;background:var(--white);color:var(--brown-dark);font-family:"Cinzel",serif;font-weight:700;font-size:16px;display:flex;align-items:center;justify-content:center}

.site-footer{position:absolute;left:0;top:2603px;width:1200px;text-align:center;font-size:17px;color:#222}
.site-footer nav{margin-top:12px;display:flex;justify-content:center;gap:10px;font-weight:700;font-size:17px}
.site-footer nav a{color:#222;text-decoration:none;font-weight:400}
</style>
</head>
<body>

<div class="greenery" style="left:60px;top:40px;width:1110px;height:560px" role="img" aria-label="Fresh herbs and leafy greens framing the header"></div>
<div class="greenery" style="left:90px;top:780px;width:1020px;height:520px" role="img" aria-label="Leafy greens framing the featured products"></div>
<div class="greenery" style="left:120px;top:2220px;width:960px;height:300px" role="img" aria-label="Leafy herbs beneath the deal banner"></div>

<div class="brand">
  <span class="brand-dot"></span>
  <span class="brand-name">Velorin</span>
</div>

<header class="main-nav">
  <nav class="nav-links">
    <a href="#">Home</a><span class="sep"></span>
    <a href="#">Products</a><span class="sep"></span>
    <a href="#">Offers</a><span class="sep"></span>
    <a href="#">Blog</a>
  </nav>
  <div class="nav-user">
    <span><svg width="18" height="18" viewBox="0 0 18 18"><circle cx="9" cy="9" r="8" fill="#222"/><circle cx="9" cy="7" r="3" fill="#7c5a1e"/><path d="M3.5 14c1.5-3 9.5-3 11 0" fill="#7c5a1e"/></svg>Account</span>
    <span><svg width="20" height="16" viewBox="0 0 20 16"><path d="M0 1h4l3 9h10l2-7H6" fill="none" stroke="#222" stroke-width="2"/><circle cx="8" cy="14" r="1.7" fill="#222"/><circle cx="16" cy="14" r="1.7" fill="#222"/></svg>Shopping Cart (0 items)</span>
  </div>
</header>

<section class="hero">
  <div class="hero-photo" role="img" aria-label="Mortar and pestle with herbal paste, neem leaves, ginger, lime and peppercorns"></div>
  <h1 class="hero-title">
    <span class="small">Your Journey to</span>
    <span class="big">NATURAL</span>
    <span class="green">LIVING</span>
  </h1>
</section>
<div class="greenery" style="left:120px;top:440px;width:170px;height:140px;border-radius:50%;background:radial-gradient(circle,#8a5a9a 0%,#b48ac0 40%,rgba(236,238,236,0) 75%)" role="img" aria-label="Purple garlic bulb with leaves"></div>

<p class="intro">Lorem Ipsum has been the industry's standard dummy text ever since the 1500s, when an unknown printer took a galley of type and scrambled it to make a type specimen book. It has survived not only five centuries, but also the leap into electronic typesetting, remaining&nbsp; unchanged</p>
<div class="intro-cta"><span class="btn-read">Read More On This Today</span></div>

<main class="panel">
  <h2 class="section-title" style="top:16px">Featured Products</h2>
  <div class="section-rule" style="top:55px"></div>

  <div class="card" style="left:38px;top:90px"><div class="card-tag">HERBAL</div><div class="card-photo photo-jar" role="img" aria-label="Herbal scrub jar"></div><div class="card-info"><div class="price">$ 24.99</div>Product Details<br>Benifits</div><div class="card-buy">BUY NOW</div></div>
  <div class="card" style="left:239px;top:90px"><div class="card-tag">HERBAL</div><div class="card-photo photo-box" role="img" aria-label="Herbal tea box"></div><div class="card-info"><div class="price">$ 24.99</div>Product Details<br>Benifits</div><div class="card-buy">BUY NOW</div></div>
  <div class="card" style="left:441px;top:90px"><div class="card-tag">ROOTS</div><div class="card-photo photo-bottle" role="img" aria-label="Root capsule bottle"></div><div class="card-info"><div class="price">$ 24.99</div>Product Details<br>Benifits</div><div class="card-buy">BUY NOW</div></div>
  <div class="card" style="left:642px;top:90px"><div class="card-tag">ROOTS</div><div class="card-photo photo-powder" role="img" aria-label="Root powder bottle with dried roots"></div><div class="card-info"><div class="price">$ 24.99</div>Product Details<br>Benifits</div><div class="card-buy">BUY NOW</div></div>

  <h2 class="section-title" style="top:421px">Latest Products</h2>
  <div class="section-rule" style="top:460px"></div>

  <div class="card" style="left:38px;top:495px"><div class="card-tag">ROOTS</div><div class="card-photo photo-powder" role="img" aria-label="Root powder bottle with dried roots"></div><div class="card-info"><div class="price">$ 24.99</div>Product Details<br>Benifits</div><div class="card-buy">BUY NOW</div></div>
  <div class="card" style="left:239px;top:495px"><div class="card-tag">ROOTS</div><div class="card-photo photo-bottle" role="img" aria-label="Root capsule bottle"></div><div class="card-info"><div class="price">$ 24.99</div>Product Details<br>Benifits</div><div class="card-buy">BUY NOW</div></div>
  <div class="card" style="left:441px;top:495px"><div class="card-tag">HERBAL</div><div class="card-photo photo-box" role="img" aria-label="Herbal tea box"></div><div class="card-info"><div class="price">$ 24.99</div>Product Details<br>Benifits</div><div class="card-buy">BUY NOW</div></div>
  <div class="card" style="left:642px;top:495px"><div class="card-tag">HERBAL</div><div class="card-photo photo-jar" role="img" aria-label="Herbal scrub jar"></div><div class="card-info"><div class="price">$ 24.99</div>Product Details<br>Benifits</div><div class="card-buy">BUY NOW</div></div>

  <h2 class="section-title" style="top:826px">Most Selling Products</h2>
  <div class="section-rule" style="top:865px"></div>

  <div class="card" style="left:38px;top:900px"><div class="card-tag">HERBAL</div><div class="card-photo photo-jar" role="img" aria-label="Herbal scrub jar"></div><div class="card-info"><div class="price">$ 24.99</div>Product Details<br>Benifits</div><div class="card-buy">BUY NOW</div></div>
  <div class="card" style="left:239px;top:900px"><div class="card-tag">HERBAL</div><div class="card-photo photo-box" role="img" aria-label="Herbal tea box"></div><div class="card-info"><div class="price">$ 24.99</div>Product Details<br>Benifits</div><div class="card-buy">BUY NOW</div></div>
  <div class="card" style="left:441px;top:900px"><div class="card-tag">ROOTS</div><div class="card-photo photo-bottle" role="img" aria-label="Root capsule bottle"></div><div class="card-info"><div class="price">$ 24.99</div>Product Details<br>Benifits</div><div class="card-buy">BUY NOW</div></div>
  <div class="card" style="left:642px;top:900px"><div class="card-tag">ROOTS</div><div class="card-photo photo-powder" role="img" aria-label="Root powder bottle with dried roots"></div><div class="card-info"><div class="price">$ 24.99</div>Product Details<br>Benifits</div><div class="card-buy">BUY NOW</div></div>

  <div class="trust">
    <span class="trust-badge"></span>
    <div class="trust-text"><b>Secure and safe</b>Online shopping</div>
  </div>
  <div class="follow">Follow Us On:</div>
  <div class="social"><span></span><span></span><span></span><span></span></div>
  <div class="divider-v"></div>

  <h3 class="newsletter-title">Newsletter</h3>
  <p class="newsletter-text">Chcete být informování o novinkách na našem<br>serveru? <b>Subscribe to our email updates</b></p>
  <div class="newsletter-form"><span class="field">Your e-mail...</span><span class="ok">OK</span></div>
</main>

<section class="deal">
  <div class="deal-photo" role="img" aria-label="Woman in an office chair holding her lower back, with a product box"></div>
  <div class="deal-text">
    <div class="h1">DEAL OF THE DAY</div>
    <div class="h2">GET INSTANT RELIEF FROM<br>MUSCLE &amp; JOINT PAIN</div>
    <div class="h3">100% NATURAL</div>
  </div>
  <span class="deal-buy">BUY NOW</span>
</section>

<footer class="site-footer">
  <div>copyright 2017 velorin, All right reserved</div>
  <nav>
    <a href="#">Home</a>|<a href="#">Help support</a>|<a href="#">Shipping rates &amp; information</a>|<a href="#">Terms &amp; Use</a>|<a href="#">FAQ</a>|<a href="#">Privacy Policy</a>
  </nav>
</footer>

</body>
</html>
```